Magnetic car sign for Harrowfield Site Advisory

I already have a logo, however I now need a design for a magnetic car sign. My company is Harrowfield Site Advisory, and I am located in Perth, Western Australia. I operate in the building and construction industry. I work largely with architects, building designers, builders, and engineers.

Target Market(s)

Everyone

Industry/Entity Type

It Company

Requirements
Nice to have
• My car is gun metal grey (dark grey). I want to sign to be based on a dark background so that it blends in with the car.

```html
<!DOCTYPE html>
<html lang="en">
<head>
<meta charset="utf-8">
<title>Harrowfield Site Advisory – Magnetic Car Sign</title>
<link rel="stylesheet" href="https://fonts.googleapis.com/css2?family=Cinzel:wght@500&family=Lato:wght@400&display=swap">
<style>
  :root {
    --car-grey: #67625d;
    --sign-white: #fbfbfa;
    --sign-rule: #9b9b9b;
    --ink: #3b3b3b;
    --ink-soft: #5a5a5a;
    --mark-red: #7c2424;
  }
  * { margin: 0; padding: 0; box-sizing: border-box; }
  html, body {
    width: 1200px;
    height: 801px;
    overflow: hidden;
    background: var(--car-grey);
  }
  .canvas {
    position: relative;
    width: 1200px;
    height: 801px;
  }
  .car-sign {
    position: absolute;
    left: 100px;
    top: 156px;
    width: 1000px;
    height: 488px;
    background: var(--sign-white);
    border-radius: 10px;
  }
  .car-sign__frame {
    position: absolute;
    inset: 18px;
    border: 3px solid var(--sign-rule);
  }
  .brand {
    position: absolute;
    left: 50px;
    top: 62px;
    display: flex;
    align-items: center;
    gap: 36px;
  }
  .brand__dot {
    width: 150px;
    height: 150px;
    border-radius: 50%;
    background: var(--mark-red);
    flex: none;
  }
  .brand__name {
    font-family: "Cinzel", serif;
    font-weight: 500;
    color: var(--ink);
    font-size: 92px;
    line-height: 1;
    letter-spacing: 2px;
  }
  .brand__rule {
    height: 3px;
    background: var(--ink);
    margin: 14px 0 10px;
  }
  .brand__tagline {
    font-family: "Cinzel", serif;
    font-weight: 500;
    color: var(--ink);
    font-size: 30px;
    letter-spacing: 9px;
    text-align: center;
  }
  .contact {
    position: absolute;
    left: 0;
    right: 0;
    top: 298px;
    font-family: "Lato", sans-serif;
    color: var(--ink);
    text-align: center;
  }
  .contact__phone {
    display: flex;
    justify-content: center;
    align-items: center;
    gap: 22px;
    font-size: 50px;
    letter-spacing: 1px;
  }
  .contact__icon {
    width: 46px;
    height: 46px;
  }
  .contact__email {
    margin-top: 14px;
    font-size: 36px;
    color: var(--ink-soft);
  }
</style>
</head>
<body>
  <main class="canvas">
    <section class="car-sign" aria-label="Magnetic car sign">
      <div class="car-sign__frame"></div>

      <header class="brand">
        <span class="brand__dot" aria-hidden="true"></span>
        <div class="brand__text">
          <h1 class="brand__name">HARROWFIELD</h1>
          <div class="brand__rule"></div>
          <p class="brand__tagline">SITE ADVISORY</p>
        </div>
      </header>

      <address class="contact" style="font-style: normal;">
        <p class="contact__phone">
          <svg class="contact__icon" viewBox="0 0 46 46" aria-hidden="true">
            <circle cx="23" cy="23" r="21" fill="none" stroke="var(--ink)" stroke-width="3"/>
            <path d="M16 13 l5 0 l2 6 l-3 2 a13 13 0 0 0 6 6 l2 -3 l6 2 l0 5 a3 3 0 0 1 -3 3 a20 20 0 0 1 -18 -18 a3 3 0 0 1 3 -3 z" fill="var(--ink)"/>
          </svg>
          <span>0400 555 173</span>
        </p>
        <p class="contact__email">Rowan.keller@harrowfieldsa.com</p>
      </address>
    </section>
  </main>
</body>
</html>
```